business card for WRT pty ltd

We require a business card that stands out . I have included our company flyer and would like the services listed to be put on the card so when we Give out the cards to customers they have an idea of services we provide. need the winning design to be in editable photo shop format, editable iMac pages format or editable windows publisher format, so that I can enter in names, email addresses, phone numbers etc myself. I have included a pdf documents of info / items needed on the card to use as reference please.
Updates

need more submissions

Need extra days to review

Sick

Target Market(s)

new customers

Contact Information for Business Card

details are on attached business card requirements file

Requirements
Must have
• I have attached a list of must haves

```html
<!DOCTYPE html>
<html lang="en">
<head>
<meta charset="UTF-8">
<title>WRT pty ltd – Business Card</title>
<link href="https://fonts.googleapis.com/css2?family=Bebas+Neue&display=swap" rel="stylesheet">
<style>
  :root {
    --black: #050505;
    --charcoal: #1c1c1e;
    --steel: #5a5d61;
    --mist: #c9cacc;
    --white: #ffffff;
    --orange: #f26a12;
    --logo-grey: #8d9094;
  }
  * { margin: 0; padding: 0; box-sizing: border-box; }
  html, body {
    width: 1200px; height: 720px; overflow: hidden;
    background: var(--black);
  }
  .card {
    position: relative; width: 1200px; height: 720px; overflow: hidden;
    background: linear-gradient(180deg, var(--charcoal) 0%, var(--steel) 45%, var(--mist) 62%, var(--steel) 100%);
    font-family: "Bebas Neue", "Oswald", sans-serif;
    color: var(--white);
  }
  .top-band {
    position: absolute; left: 0; top: 0; width: 1200px; height: 126px;
    background: var(--black);
  }
  .stripe { position: absolute; height: 22px; }
  .stripe--white-left { left: 0; top: 128px; width: 420px; background: linear-gradient(90deg, var(--white) 55%, rgba(255,255,255,0)); }
  .stripe--white-right { right: 0; top: 128px; width: 420px; background: linear-gradient(270deg, var(--white) 55%, rgba(255,255,255,0)); }
  .stripe--orange-left { left: 0; top: 168px; width: 420px; height: 9px; background: linear-gradient(90deg, var(--orange) 60%, rgba(242,106,18,0)); }
  .stripe--orange-right { right: 0; top: 168px; width: 420px; height: 9px; background: linear-gradient(270deg, var(--orange) 60%, rgba(242,106,18,0)); }
  .logo-panel {
    position: absolute; left: 300px; top: 0; width: 600px; height: 360px;
    background: radial-gradient(ellipse at 50% 45%, #4a4c50 0%, #2a2b2e 45%, rgba(40,40,42,0) 75%);
  }
  .orange-sweep { position: absolute; left: 0; top: 0; }
  .truck-photo {
    position: absolute; left: 83px; top: 250px; width: 1032px; height: 225px;
    background: linear-gradient(180deg, #2b2d2f 0%, #151617 60%, #0c0c0c 100%);
    clip-path: polygon(0 0, 100% 20%, 100% 62%, 55% 68%, 20% 100%, 0 100%);
  }
  .logo-name {
    position: absolute; left: 0; top: 96px; width: 1200px; text-align: center;
    font-size: 200px; line-height: 1; letter-spacing: 6px;
    color: var(--logo-grey);
    z-index: 2;
  }
  .person-name {
    position: absolute; right: 80px; top: 436px;
    font-size: 52px; letter-spacing: 1px; line-height: 1;
    z-index: 2;
  }
  .contact { position: absolute; font-size: 44px; line-height: 52px; letter-spacing: 0.5px; z-index: 2; }
  .contact--left { left: 83px; top: 490px; }
  .contact--right { right: 80px; top: 542px; text-align: right; }
</style>
</head>
<body>
  <div class="card">
    <div class="top-band"></div>
    <div class="stripe stripe--white-left"></div>
    <div class="stripe stripe--white-right"></div>
    <div class="stripe stripe--orange-left"></div>
    <div class="stripe stripe--orange-right"></div>

    <div class="logo-panel" role="img" aria-label="Dark metallic honeycomb texture behind the company name"></div>

    <svg class="orange-sweep" width="1200" height="720" viewBox="0 0 1200 720" aria-hidden="true">
      <defs>
        <linearGradient id="sweepFill" x1="0" y1="0" x2="0.15" y2="1">
          <stop offset="0" stop-color="#3a2414"/>
          <stop offset="0.35" stop-color="#5a3015"/>
          <stop offset="0.7" stop-color="#d85e10"/>
          <stop offset="1" stop-color="#f26a12"/>
        </linearGradient>
      </defs>
      <path d="M0,470 C300,330 700,260 1200,285 L1200,720 L0,720 Z" fill="url(#sweepFill)"/>
    </svg>

    <div class="truck-photo" role="img" aria-label="Photo of a black road train truck hauling three side-tipper trailers"></div>

    <div class="logo-name">WRT</div>

    <div class="person-name">Daniel Horvat (Director)</div>

    <div class="contact contact--left">
      <p>Phone: 0400 123 987</p>
      <p>Email: email@wrtservices.com.au</p>
      <p>Website: www.wrtservices.com.au</p>
    </div>

    <div class="contact contact--right">
      <p>Depot: Lot 27</p>
      <p>Haulage Road Australia</p>
    </div>
  </div>
</body>
</html>
```